NEW Brand "New Zealand Wine Estate"

We are looking for a design for our new range of New Zealand wine. An estate label that can be used for several varietals.
We have three potential names...
Hollow Pine Estate
Velvet Morrow Estate
Tovrina Estate
first variant is "Central Otago Pinot Noir" please use this in the original design.
This brand is for world export, so will need to be appealing to many markets but representative of New Zealand and our rugged Coasts.
Target Market(s)
Supermarket $25 NZD per bottle price point. Young and hip
Font styles to use
Decorative
Script
Requirements
Must have
- Sophistication but edgy. Stand out on a shelf.
- the brand needs to be able to be used for red or white wine.

```html
<!DOCTYPE html>
<html lang="en">
<head>
<meta charset="utf-8">
<title>Central Otago Pinot Noir — Wine Label</title>
<link rel="stylesheet" href="https://fonts.googleapis.com/css2?family=Raleway:wght@400;500&family=Roboto:wght@700&family=Yellowtail&family=Damion&display=block">
<style>
  :root {
    --page: #ffffff;
    --stamp: #edebed;
    --frame: #ffffff;
    --navy: #0d1a8c;
    --slate-blue: #5a64b4;
    --fern: #4f5bbb;
    --fern-light: #8c93cf;
    --fern-faint: #d9d9ea;
    --map-tone: #e4e3e9;
    --title-white: #ffffff;
  }
  * { margin: 0; padding: 0; box-sizing: border-box; }
  html, body {
    width: 851px;
    height: 1200px;
    overflow: hidden;
    background: var(--page);
  }
  .label {
    position: relative;
    width: 851px;
    height: 1200px;
  }
  .stamp-shape {
    position: absolute;
    inset: 0;
  }
  .art-layer {
    position: absolute;
    left: 11px;
    top: 11px;
    width: 829px;
    height: 1178px;
    overflow: hidden;
  }
  .art {
    position: absolute;
  }
  .map-art {
    left: 90px;
    top: 70px;
    width: 520px;
    height: 990px;
    border-radius: 40% 50% 45% 55% / 30% 35% 40% 45%;
    background: linear-gradient(160deg, var(--map-tone), rgba(228, 227, 233, 0.3));
    opacity: 0.6;
  }
  .fern-faint {
    left: 480px;
    top: 780px;
    width: 330px;
    height: 390px;
    border-radius: 50%;
    background: radial-gradient(closest-side, var(--fern-faint), rgba(217, 217, 234, 0));
  }
  .fern-top-left {
    left: 0;
    top: 0;
    width: 290px;
    height: 280px;
    border-radius: 0 0 70% 30% / 0 0 60% 40%;
    background: linear-gradient(135deg, var(--fern) 0%, var(--fern-light) 70%, rgba(140, 147, 207, 0.4) 100%);
    opacity: 0.85;
  }
  .fern-top-right {
    left: 600px;
    top: 0;
    width: 229px;
    height: 210px;
    border-radius: 0 0 0 75% / 0 0 0 70%;
    background: linear-gradient(225deg, var(--fern) 0%, var(--fern-light) 80%, rgba(140, 147, 207, 0.4) 100%);
    opacity: 0.85;
  }
  .fern-right-mid {
    left: 720px;
    top: 220px;
    width: 109px;
    height: 210px;
    border-radius: 60% 0 0 60% / 50% 0 0 50%;
    background: linear-gradient(270deg, var(--fern) 0%, var(--fern-light) 100%);
    opacity: 0.85;
  }
  .fern-right-low {
    left: 645px;
    top: 460px;
    width: 184px;
    height: 230px;
    border-radius: 55% 0 0 70% / 45% 0 0 60%;
    background: linear-gradient(250deg, var(--fern) 0%, var(--fern-light) 85%, rgba(140, 147, 207, 0.5) 100%);
    opacity: 0.85;
  }
  .fern-left {
    left: 0;
    top: 250px;
    width: 160px;
    height: 550px;
    border-radius: 0 70% 60% 0 / 0 40% 40% 0;
    background: linear-gradient(90deg, var(--fern) 0%, var(--fern-light) 80%, rgba(140, 147, 207, 0.4) 100%);
    opacity: 0.85;
  }
  .fern-left-soft {
    left: 120px;
    top: 240px;
    width: 230px;
    height: 300px;
    border-radius: 50%;
    background: radial-gradient(closest-side, rgba(140, 147, 207, 0.45), rgba(140, 147, 207, 0));
  }
  .inner-frame {
    position: absolute;
    left: 64px;
    top: 68px;
    width: 728px;
    height: 1048px;
    border: 5px solid var(--frame);
  }
  .country {
    position: absolute;
    top: 278px;
    left: 0;
    width: 851px;
    padding-left: 0.3em;
    text-align: center;
    font-family: "Raleway", sans-serif;
    font-weight: 500;
    font-size: 17px;
    line-height: 20px;
    letter-spacing: 0.32em;
    color: var(--slate-blue);
  }
  .region-top {
    position: absolute;
    top: 374px;
    left: 0;
    width: 851px;
    padding-left: 0.6em;
    text-align: center;
    font-family: "Raleway", sans-serif;
    font-weight: 400;
    font-size: 44px;
    line-height: 50px;
    letter-spacing: 0.6em;
    color: var(--navy);
  }
  .region-main {
    position: absolute;
    top: 420px;
    left: 0;
    width: 851px;
    text-align: center;
    font-family: "Roboto", sans-serif;
    font-weight: 700;
    font-size: 200px;
    line-height: 1;
    letter-spacing: -0.01em;
    color: var(--title-white);
  }
  .varietal {
    position: absolute;
    top: 762px;
    left: 0;
    width: 851px;
    text-align: center;
    font-family: "Yellowtail", "Damion", cursive;
    font-size: 78px;
    line-height: 1;
    color: var(--navy);
  }
</style>
</head>
<body>
  <main class="label">
    <svg class="stamp-shape" width="851" height="1200" viewBox="0 0 851 1200" aria-hidden="true">
      <rect x="11" y="11" width="829" height="1178" fill="var(--stamp)"/>
    </svg>

    <div class="art-layer">
      <div class="art map-art" role="img" aria-label="Faint grey outline map of New Zealand"></div>
      <div class="art fern-faint" role="img" aria-label="Faint silver fern fronds"></div>
      <div class="art fern-left-soft" role="img" aria-label="Soft translucent fern frond"></div>
      <div class="art fern-top-left" role="img" aria-label="Blue silver fern fronds in the top left corner"></div>
      <div class="art fern-top-right" role="img" aria-label="Blue silver fern fronds in the top right corner"></div>
      <div class="art fern-right-mid" role="img" aria-label="Blue silver fern frond on the right edge"></div>
      <div class="art fern-right-low" role="img" aria-label="Blue silver fern frond on the lower right"></div>
      <div class="art fern-left" role="img" aria-label="Blue silver fern fronds along the left edge"></div>
    </div>

    <svg class="stamp-shape" width="851" height="1200" viewBox="0 0 851 1200" aria-hidden="true">
      <g fill="var(--page)">
        <circle cx="94" cy="11" r="24"/><circle cx="204" cy="11" r="24"/><circle cx="314" cy="11" r="24"/>
        <circle cx="424" cy="11" r="24"/><circle cx="534" cy="11" r="24"/><circle cx="644" cy="11" r="24"/>
        <circle cx="754" cy="11" r="24"/>
        <circle cx="94" cy="1189" r="24"/><circle cx="204" cy="1189" r="24"/><circle cx="314" cy="1189" r="24"/>
        <circle cx="424" cy="1189" r="24"/><circle cx="534" cy="1189" r="24"/><circle cx="644" cy="1189" r="24"/>
        <circle cx="754" cy="1189" r="24"/>
        <circle cx="11" cy="97" r="24"/><circle cx="11" cy="207" r="24"/><circle cx="11" cy="317" r="24"/>
        <circle cx="11" cy="427" r="24"/><circle cx="11" cy="537" r="24"/><circle cx="11" cy="647" r="24"/>
        <circle cx="11" cy="757" r="24"/><circle cx="11" cy="867" r="24"/><circle cx="11" cy="977" r="24"/>
        <circle cx="11" cy="1087" r="24"/>
        <circle cx="840" cy="97" r="24"/><circle cx="840" cy="207" r="24"/><circle cx="840" cy="317" r="24"/>
        <circle cx="840" cy="427" r="24"/><circle cx="840" cy="537" r="24"/><circle cx="840" cy="647" r="24"/>
        <circle cx="840" cy="757" r="24"/><circle cx="840" cy="867" r="24"/><circle cx="840" cy="977" r="24"/>
        <circle cx="840" cy="1087" r="24"/>
      </g>
    </svg>

    <div class="inner-frame"></div>

    <p class="country">NEW ZEALAND</p>
    <p class="region-top">CENTRAL</p>
    <h1 class="region-main">OTAGO</h1>
    <p class="varietal">Pinot Noir</p>
  </main>
</body>
</html>
```